Fitness center graphic design

Looking for graphics to complete interior of a gym
img 3133 - main entrance, looking for something motivational, eye catching. can include logo but prefer not to
img 9617 looking for something to encourage heavy lifting. something motivating
img 9616 is across from 9617 location. maybe something with logo
img 9614 seen upon entering want something that highlights all our offerings. put a photo for inspriation only
img b37 is streching zone. want it to be labled
img b76 personal training/ group training room. want it to be labled
Updates

Target Market(s)

Want graphics to be eye catching. And appeal to all fitness levels

Industry/Entity Type

Fitness gym

Requirements
Must have
• eye catching, bright, motivating qualities
Should not have
• logo in every design

```html
<!DOCTYPE html>
<html lang="en">
<head>
<meta charset="utf-8">
<title>Gym Interior Graphics – Placement Board</title>
<link href="https://fonts.googleapis.com/css2?family=Oswald:wght@400;500;600&display=swap" rel="stylesheet">
<style>
  :root {
    --orange: #f04e23;
    --black: #0b0b0b;
    --white: #ffffff;
    --paper: #ffffff;
    --caption: #1a1a1a;
  }
  html, body { margin: 0; padding: 0; overflow: hidden; background: var(--paper); }
  .board {
    position: relative; width: 1200px; height: 849px; overflow: hidden;
    background: var(--paper); font-family: "Oswald", sans-serif;
  }
  .art { position: absolute; left: 0; top: 0; }
  .txt { position: absolute; margin: 0; text-transform: uppercase; font-weight: 600; letter-spacing: 0.5px; line-height: 1.15; }
  .headline-top { left: 163px; top: 74px; font-size: 21px; color: var(--white); letter-spacing: 1px; }
  .offer-title { left: 618px; top: 173px; font-size: 16.5px; color: var(--orange); }
  .offer-copy { left: 618px; top: 252px; width: 150px; font-size: 3.6px; line-height: 1.3; color: var(--white); text-transform: none; font-weight: 400; letter-spacing: 0; }
  .weak-quote { left: 258px; top: 586px; font-size: 17px; color: var(--white); }
  .brand-name { left: 846px; top: 378px; font-size: 16px; color: var(--white); font-weight: 500; letter-spacing: 1px; line-height: 1; }
  .brand-name span { display: block; font-size: 9px; letter-spacing: 9px; margin-top: 3px; padding-left: 44px; }
  .stretch-label { left: 876px; top: 498px; font-size: 17px; color: var(--white); transform: rotate(-33deg); transform-origin: center; text-align: left; line-height: 1.05; }
  .training-label { left: 974px; top: 653px; width: 137px; text-align: center; font-size: 15px; color: var(--white); letter-spacing: 1px; }
  .photo-caption { position: absolute; font-size: 11.5px; color: var(--caption); font-weight: 400; transform: translateX(-50%); }
</style>
</head>
<body>
<div class="board">
  <svg class="art" width="1200" height="849" viewBox="0 0 1200 849" xmlns="http://www.w3.org/2000/svg">
    <defs>
      <linearGradient id="gym-blue" x1="0" y1="0" x2="0" y2="1"><stop offset="0" stop-color="#c9b98f"/><stop offset="0.35" stop-color="#3a4a9a"/><stop offset="1" stop-color="#55565a"/></linearGradient>
      <linearGradient id="gym-glass" x1="0" y1="0" x2="0" y2="1"><stop offset="0" stop-color="#e8ece9"/><stop offset="0.6" stop-color="#b9cbc6"/><stop offset="1" stop-color="#4b4a48"/></linearGradient>
      <linearGradient id="gym-red" x1="0" y1="0" x2="0" y2="1"><stop offset="0" stop-color="#e9e4dc"/><stop offset="0.45" stop-color="#b8584c"/><stop offset="1" stop-color="#2d2d2f"/></linearGradient>
      <linearGradient id="gym-carpet" x1="0" y1="0" x2="0" y2="1"><stop offset="0" stop-color="#e7e3db"/><stop offset="0.55" stop-color="#c9c3ba"/><stop offset="1" stop-color="#2e2e30"/></linearGradient>
      <linearGradient id="gym-lobby" x1="0" y1="0" x2="0" y2="1"><stop offset="0" stop-color="#d8cfbd"/><stop offset="0.6" stop-color="#8c7a63"/><stop offset="1" stop-color="#c2a77a"/></linearGradient>
      <linearGradient id="figure-tone" x1="0" y1="0" x2="0" y2="1"><stop offset="0" stop-color="#e7c3a4"/><stop offset="1" stop-color="#d9dfe6"/></linearGradient>
    </defs>

    <!-- Banner: body achieves -->
    <g class="banner-mind">
      <rect x="54" y="60" width="642" height="58" fill="var(--black)"/>
      <polygon points="54,60 128,60 74,118 54,118" fill="var(--orange)"/>
      <polygon points="140,118 190,100 200,100 156,118" fill="var(--orange)"/>
      <polygon points="352,66 362,60 396,60 386,66" fill="var(--orange)"/>
      <polygon points="390,118 420,104 436,104 406,118" fill="var(--orange)"/>
      <polygon points="560,118 696,60 696,118" fill="var(--orange)"/>
      <polygon points="520,118 550,105 562,105 532,118" fill="var(--orange)"/>
      <rect x="65" y="61" width="86" height="57" fill="url(#figure-tone)" role="img" aria-label="Illustration of a man bench pressing a barbell"/>
      <rect x="609" y="61" width="70" height="57" fill="url(#figure-tone)" role="img" aria-label="Illustration of a woman using a cable pulldown machine"/>
    </g>

    <!-- Site photos -->
    <rect x="133" y="148" width="219" height="164" fill="url(#gym-blue)" role="img" aria-label="Site photo 9313: main entrance with blue overhead band above weight machines"/>
    <rect x="353" y="148" width="219" height="164" fill="url(#gym-glass)" role="img" aria-label="Site photo 9614: frosted glass wall seen on entering"/>
    <rect x="133" y="351" width="219" height="164" fill="url(#gym-red)" role="img" aria-label="Site photo 9616: mirrored wall with red panel"/>
    <rect x="353" y="351" width="219" height="164" fill="url(#gym-red)" role="img" aria-label="Site photo 9617: free weights area with red wall"/>
    <rect x="636" y="458" width="222" height="163" fill="url(#gym-carpet)" role="img" aria-label="Site photo b37: stretching room with dark carpet"/>
    <rect x="974" y="458" width="137" height="163" fill="url(#gym-lobby)" role="img" aria-label="Site photo: doorway to the training room"/>

    <!-- Banner: offerings -->
    <g class="banner-offerings">
      <rect x="583" y="148" width="482" height="163" fill="var(--black)"/>
      <polygon points="1035,148 1065,148 1065,170" fill="var(--orange)"/>
      <polygon points="830,311 1065,188 1065,311" fill="var(--orange)"/>
      <polygon points="740,311 820,268 838,268 758,311" fill="var(--orange)"/>
      <polygon points="780,311 850,272 862,272 792,311" fill="var(--orange)"/>
      <g role="img" aria-label="Row of seven small photos of gym offerings">
        <rect x="618" y="220" width="34" height="25" fill="#8c8a86"/>
        <rect x="655.5" y="220" width="34" height="25" fill="#8c8a86"/>
        <rect x="693" y="220" width="34" height="25" fill="#8c8a86"/>
        <rect x="730.5" y="220" width="34" height="25" fill="#8c8a86"/>
        <rect x="768" y="220" width="34" height="25" fill="#8c8a86"/>
        <rect x="805.5" y="220" width="34" height="25" fill="#8c8a86"/>
        <rect x="843" y="220" width="34" height="25" fill="#8c8a86"/>
      </g>
      <rect x="958" y="164" width="105" height="147" fill="url(#figure-tone)" role="img" aria-label="Illustration of a man lifting dumbbells overhead"/>
    </g>

    <!-- Banner: bench illustration -->
    <g class="banner-bench">
      <rect x="583" y="351" width="182" height="77" fill="var(--black)"/>
      <polygon points="583,351 690,351 625,428 583,428" fill="var(--orange)"/>
      <polygon points="720,428 765,398 765,428" fill="var(--orange)"/>
      <rect x="602" y="352" width="123" height="76" fill="url(#figure-tone)" role="img" aria-label="Illustration of a woman lying on a bench with dumbbells"/>
    </g>

    <!-- Banner: brand -->
    <g class="banner-brand">
      <rect x="788" y="351" width="277" height="77" fill="var(--black)"/>
      <polygon points="1010,351 1040,351 1022,362 992,362" fill="var(--orange)"/>
      <polygon points="975,428 1065,370 1065,428" fill="var(--orange)"/>
      <polygon points="940,428 1000,392 1012,392 952,428" fill="var(--orange)"/>
      <circle cx="828" cy="390" r="12" fill="var(--orange)"/>
    </g>

    <!-- Stretching zone panel -->
    <g class="panel-stretch">
      <rect x="872" y="456" width="88" height="165" fill="var(--orange)"/>
      <polygon points="872,568 960,508 960,585 872,621" fill="var(--black)"/>
      <polygon points="905,621 960,590 960,621" fill="var(--orange)"/>
    </g>

    <!-- Training zone door frame -->
    <g class="frame-training">
      <rect x="974" y="648" width="137" height="143" fill="var(--orange)"/>
      <rect x="992" y="678" width="101" height="113" fill="var(--white)"/>
      <polygon points="974,745 992,733 992,791 974,791" fill="var(--black)"/>
      <polygon points="1093,690 1111,676 1111,725 1093,737" fill="var(--black)"/>
      <polygon points="1075,678 1093,666 1111,666 1111,672 1093,678" fill="var(--black)"/>
    </g>

    <!-- Banner: being weak -->
    <g class="banner-weak">
      <rect x="133" y="565" width="481" height="77" fill="var(--orange)"/>
      <polygon points="133,565 175,565 133,595" fill="var(--black)"/>
      <polygon points="133,625 160,608 175,608 148,642 133,642" fill="var(--black)"/>
      <polygon points="235,608 300,565 345,565 250,618" fill="var(--black)"/>
      <polygon points="520,642 614,590 614,642" fill="var(--black)"/>
      <polygon points="500,642 560,610 570,610 512,642" fill="var(--black)"/>
      <rect x="157" y="566" width="76" height="76" fill="url(#figure-tone)" role="img" aria-label="Illustration of a woman lifting a barbell"/>
    </g>

    <!-- Placement connectors -->
    <g class="connectors" stroke="var(--orange)" stroke-width="1.2" fill="none">
      <line x1="383" y1="118" x2="265" y2="185"/>
      <line x1="479" y1="224" x2="583" y2="224"/>
      <line x1="210" y1="418" x2="210" y2="565"/>
      <line x1="823" y1="485" x2="872" y2="485"/>
      <line x1="1039" y1="490" x2="1039" y2="648"/>
    </g>
    <line x1="479" y1="423" x2="583" y2="402" stroke="var(--black)" stroke-width="1"/>
    <g class="pins" fill="var(--orange)">
      <circle cx="265" cy="185" r="5"/>
      <circle cx="479" cy="224" r="5"/>
      <circle cx="210" cy="418" r="5"/>
      <circle cx="823" cy="485" r="5"/>
      <circle cx="1039" cy="490" r="5"/>
    </g>
    <circle cx="479" cy="423" r="5" fill="var(--black)"/>
  </svg>

  <p class="txt headline-top">The body achieves what the mind believes</p>
  <p class="txt offer-title">Your body can stand almost anything<br>It’s your mind that you have to convince</p>
  <p class="txt offer-copy">Strength classes, cardio floor, free weights, personal coaching, group sessions and a calm stretching area. Open early and late every day for members of all levels. Book a tour at the front desk and start training with our friendly team this week.</p>
  <p class="txt brand-name">Summit Fitness<span>Club</span></p>
  <p class="txt stretch-label">Streching<br>zone</p>
  <p class="txt training-label">Training zone</p>
  <p class="txt weak-quote">If you think lifting weights is dangerous,<br>try being weak. Being weak is dangerous</p>

  <span class="photo-caption" style="left:243px;top:322px">9313</span>
  <span class="photo-caption" style="left:474px;top:322px">9614</span>
  <span class="photo-caption" style="left:243px;top:528px">9616</span>
  <span class="photo-caption" style="left:474px;top:528px">9617</span>
  <span class="photo-caption" style="left:748px;top:630px">b37</span>
</div>
</body>
</html>
```